Packaging for Hair Fibers Product

We are a start up company looking for a new packaging design for hair building fibers. These are aimed at predominantly men but also women as well. We already have a logo and i have the packaging design from our competitors. We are wanting to keep the look masculine as 90% of our users will be middle aged men. We would like the colours to be black and white but are open to other colours as well.
It will need to have our logo and the following somewhere on the front.
"Instant Fuller & Thicker Hair" & "Natural Hair Building Fibers" "28g" or "Net Weight 28g"
We only need the front of the packaging designed, please make the other sides of the packaging the same colour but blank.
Target Market(s)
Men 25+
Industry/Entity Type
Hair And Beauty
Requirements
Must have
- Logo which i have included. and the following somewhere on the front.
- "Instant Fuller & Thicker Hair" ; "Natural Hair Building Fibers" "28g" or "Net Weight 28g"
Nice to have
- Make it stand out from the competition or similar to the palirox example.

```html
<!DOCTYPE html>
<html lang="en">
<head>
<meta charset="utf-8">
<title>Folliq – Hair Building Fibers Carton Dieline</title>
<link rel="stylesheet" href="https://fonts.googleapis.com/css2?family=Open+Sans:wght@400;600&family=Roboto:wght@400;500&display=swap">
<style>
  :root {
    --carton-black: #231f20;
    --paper-white: #ffffff;
    --fold-line: #3d393a;
    --measure-line: #231f20;
    --glue-edge: #9a9a9a;
  }
  html, body {
    margin: 0;
    padding: 0;
    width: 1200px;
    height: 1200px;
    overflow: hidden;
    background: var(--paper-white);
  }
  .dieline {
    display: block;
    width: 1200px;
    height: 1200px;
  }
  .panel { fill: var(--carton-black); }
  .fold { stroke: var(--fold-line); stroke-width: 1.2; fill: none; }
  .glue-flap { fill: var(--paper-white); stroke: var(--glue-edge); stroke-width: 1; }
  .measure { stroke: var(--measure-line); stroke-width: 1.2; fill: none; }
  .measure-label {
    font-family: "Roboto", Arial, sans-serif;
    font-size: 30px;
    fill: var(--measure-line);
  }
  .logo-band { fill: var(--paper-white); }
  .brand-name {
    font-family: "Open Sans", Arial, sans-serif;
    font-weight: 400;
    font-size: 44px;
    letter-spacing: 6px;
    fill: var(--carton-black);
  }
  .descriptor {
    font-family: "Roboto", Arial, sans-serif;
    font-weight: 500;
    font-size: 15px;
    fill: var(--paper-white);
  }
  .claim {
    font-family: "Open Sans", Arial, sans-serif;
    font-weight: 400;
    font-size: 28px;
    letter-spacing: 1px;
    fill: var(--paper-white);
  }
  .audience-badge { fill: var(--paper-white); }
  .audience-text {
    font-family: "Roboto", Arial, sans-serif;
    font-size: 16px;
    fill: var(--carton-black);
  }
  .net-weight {
    font-family: "Roboto", Arial, sans-serif;
    font-size: 21px;
    fill: var(--paper-white);
  }
</style>
</head>
<body>
<svg class="dieline" viewBox="0 0 1500 1500" xmlns="http://www.w3.org/2000/svg" aria-label="Folliq hair building fibers carton dieline">

  <!-- Measurements -->
  <g class="measurements">
    <line class="measure" x1="191" y1="50" x2="191" y2="600"/>
    <line class="measure" x1="490" y1="50" x2="490" y2="228"/>
    <line class="measure" x1="191" y1="78" x2="240" y2="78"/>
    <line class="measure" x1="413" y1="78" x2="490" y2="78"/>
    <text class="measure-label" x="328" y="90" text-anchor="middle">5.2 cm</text>

    <line class="measure" x1="789" y1="87" x2="789" y2="268"/>
    <line class="measure" x1="490" y1="115" x2="567" y2="115"/>
    <line class="measure" x1="739" y1="115" x2="789" y2="115"/>
    <text class="measure-label" x="653" y="127" text-anchor="middle">5.2 cm</text>

    <line class="measure" x1="97" y1="611" x2="177" y2="611"/>
    <line class="measure" x1="97" y1="1164" x2="177" y2="1164"/>
    <line class="measure" x1="126" y1="611" x2="126" y2="787"/>
    <line class="measure" x1="126" y1="968" x2="126" y2="1164"/>
    <text class="measure-label" x="126" y="880" text-anchor="middle" dominant-baseline="middle" transform="rotate(-90 126 880)">9.6 cm</text>
  </g>

  <!-- Glue flap -->
  <polygon class="glue-flap" points="1385,611 1455,626 1455,1148 1385,1164"/>

  <!-- Top flaps -->
  <path class="panel top-tuck" d="M490,611 V240 Q490,228 502,228 H777 Q789,228 789,240 V611 Z"/>
  <path class="panel dust-flap-left" d="M191,611 V563 L218,540 V458 Q218,438 240,438 H462 V583 L490,611 Z"/>
  <path class="panel dust-flap-right" d="M789,611 L816,583 V438 H1038 Q1060,438 1060,458 V540 L1087,563 V611 Z"/>

  <!-- Body panels -->
  <rect class="panel side-panel" x="191" y="611" width="299" height="553"/>
  <rect class="panel front-panel" x="490" y="611" width="299" height="553"/>
  <rect class="panel side-panel" x="789" y="611" width="298" height="553"/>
  <rect class="panel back-panel" x="1087" y="611" width="298" height="553"/>

  <!-- Bottom flaps -->
  <path class="panel bottom-flap-left" d="M191,1164 H490 L341,1238 V1299 Q341,1307 333,1307 H191 Z"/>
  <path class="panel bottom-tuck" d="M490,1164 H789 V1393 H705 V1308 H574 V1393 H490 Z"/>
  <path class="panel bottom-flap-right" d="M789,1164 H1087 V1307 H945 Q937,1307 937,1299 V1238 Z"/>
  <polygon class="panel bottom-lock" points="1087,1164 1385,1164 1303,1305 1303,1393 1170,1393 1170,1305"/>

  <!-- Fold lines -->
  <g class="folds">
    <line class="fold" x1="191" y1="611" x2="1385" y2="611"/>
    <line class="fold" x1="191" y1="1164" x2="1385" y2="1164"/>
    <line class="fold" x1="490" y1="611" x2="490" y2="1164"/>
    <line class="fold" x1="789" y1="611" x2="789" y2="1164"/>
    <line class="fold" x1="1087" y1="611" x2="1087" y2="1164"/>
    <line class="fold" x1="490" y1="312" x2="789" y2="312"/>
  </g>

  <!-- Top panel branding (reads upright when closed) -->
  <g class="top-branding" transform="rotate(180 639.5 430)">
    <rect class="logo-band" x="490" y="363" width="299" height="87"/>
    <text class="brand-name" x="639.5" y="422" text-anchor="middle">FOLLIQ</text>
    <text class="descriptor" x="639.5" y="469" text-anchor="middle">Natural Hair Building Fibers</text>
  </g>

  <!-- Front panel -->
  <g class="front-branding">
    <rect class="logo-band" x="490" y="749" width="299" height="85"/>
    <text class="brand-name" x="639.5" y="807" text-anchor="middle">FOLLIQ</text>
    <text class="descriptor" x="639.5" y="863" text-anchor="middle">Natural Hair Building Fibers</text>
    <text class="claim" x="633" y="938" text-anchor="middle">Instant Fuller</text>
    <text class="claim" x="639" y="978" text-anchor="middle">&amp; Thicker Hair</text>
    <circle class="audience-badge" cx="639.5" cy="1056" r="34"/>
    <text class="audience-text" x="639.5" y="1050" text-anchor="middle">FOR</text>
    <text class="audience-text" x="639.5" y="1070" text-anchor="middle">MEN</text>
    <text class="net-weight" x="639.5" y="1133" text-anchor="middle">28g</text>
  </g>
</svg>
</body>
</html>
```